Business card

We are looking for a creative person to deigns our company business card.

Target Market(s)

College age student

Industry/Entity Type

Accommodation

Contact Information for Business Card

We want a fun, clean and sophisticated design. It should look good, but more importantly the information should be legible.

Font styles to use
Serif
Sans Serif
Other font styles liked:
• Open Sans ,

Colors
33a6d7

Requirements
Must have
• Must have a young and memorable message. Be legible.
• Our logo on the back on a solid blue , please find color and logo attached
• LodgeBridgely.net on the back.
Nice to have
• I would like to have couple of different fonts on the LodgeBridgely.net on the back of the cards with a solid blue.

```html
<!DOCTYPE html>
<html lang="en">
<head>
<meta charset="utf-8">
<title>LodgeBridgely Business Card</title>
<link rel="stylesheet" href="https://fonts.googleapis.com/css2?family=Open+Sans:wght@400;600;700&family=PT+Serif:wght@400&display=swap">
<style>
  :root {
    --bg: #9a9a9a;
    --navy: #10507e;
    --navy-deep: #0c4670;
    --mid-blue: #3389c6;
    --brand-blue: #33a6d7;
    --white: #ffffff;
    --paper-top: #ffffff;
    --paper-bottom: #e4e4e4;
    --ink: #333333;
    --rule: #9a9a9a;
    --url-grey: #c9d3dc;
  }
  * { box-sizing: border-box; margin: 0; padding: 0; }
  html, body { width: 1200px; height: 900px; overflow: hidden; }
  body {
    background: var(--bg);
    font-family: "Open Sans", Arial, sans-serif;
    position: relative;
  }
  .card {
    position: absolute;
    left: 285px;
    width: 630px;
    height: 360px;
    border-radius: 22px;
    overflow: hidden;
  }
  /* Back side */
  .card-back {
    top: 60px;
    background: var(--navy);
  }
  .back-name {
    position: absolute;
    left: 48px;
    top: 210px;
    font-family: "Open Sans", Arial, sans-serif;
    font-weight: 700;
    font-size: 34px;
    color: var(--mid-blue);
    display: flex;
    align-items: center;
    gap: 14px;
  }
  .back-name .mark {
    width: 28px;
    height: 28px;
    background: var(--mid-blue);
  }
  .back-url {
    position: absolute;
    right: 48px;
    top: 160px;
    font-family: "PT Serif", Georgia, serif;
    font-size: 24px;
    color: var(--url-grey);
  }
  .back-url .url-name { color: var(--mid-blue); }

  /* Front side */
  .card-front {
    top: 480px;
    background: linear-gradient(180deg, var(--paper-top) 0%, var(--paper-bottom) 100%);
  }
  .brand {
    position: absolute;
    left: 40px;
    top: 150px;
    display: flex;
    align-items: center;
    gap: 10px;
    font-weight: 700;
    font-size: 26px;
    color: var(--navy);
  }
  .brand .mark {
    width: 22px;
    height: 22px;
    background: var(--mid-blue);
  }
  .divider {
    position: absolute;
    left: 292px;
    top: 44px;
    width: 1px;
    height: 170px;
    background: var(--rule);
  }
  .details {
    position: absolute;
    left: 316px;
    top: 34px;
    color: var(--ink);
  }
  .person-name {
    font-weight: 600;
    font-size: 30px;
    line-height: 1.1;
    color: var(--navy);
  }
  .person-title {
    font-size: 18px;
    font-weight: 600;
    color: #444;
    margin-bottom: 10px;
  }
  .address {
    font-size: 13px;
    line-height: 1.45;
    margin-bottom: 8px;
  }
  .contact-list { list-style: none; font-size: 13px; line-height: 1.6; }
  .contact-list li { display: flex; align-items: center; gap: 8px; }
  .contact-list svg { width: 12px; height: 12px; fill: var(--navy); flex: none; }
  .tagline-band {
    position: absolute;
    left: 0;
    right: 0;
    top: 262px;
    height: 40px;
    background: var(--navy-deep);
    color: var(--white);
    font-size: 15px;
    display: flex;
    align-items: center;
    justify-content: center;
    letter-spacing: 0.2px;
  }
  .band-line {
    position: absolute;
    left: 0;
    right: 0;
    height: 2px;
    background: var(--mid-blue);
  }
  .band-line.upper { top: 255px; }
  .band-line.lower { top: 308px; }
</style>
</head>
<body>
  <section class="card card-back" aria-label="Card back">
    <div class="back-name"><span class="mark"></span>LodgeBridgely</div>
    <div class="back-url">www.<span class="url-name">LodgeBridgely</span>.net</div>
  </section>

  <section class="card card-front" aria-label="Card front">
    <div class="brand"><span class="mark"></span>LodgeBridgely</div>
    <div class="divider"></div>
    <div class="details">
      <div class="person-name">Daniel Hart</div>
      <div class="person-title">President</div>
      <div class="address">Level 2, 17 Harbour Lane<br>Brightwater, VIC 3999</div>
      <ul class="contact-list">
        <li><svg viewBox="0 0 24 24" aria-hidden="true"><path d="M6.6 10.8a15 15 0 0 0 6.6 6.6l2.2-2.2a1 1 0 0 1 1-.25 11.4 11.4 0 0 0 3.6.57 1 1 0 0 1 1 1V20a1 1 0 0 1-1 1A17 17 0 0 1 3 4a1 1 0 0 1 1-1h3.5a1 1 0 0 1 1 1c0 1.25.2 2.45.57 3.6a1 1 0 0 1-.25 1z"/></svg>555 018 2746</li>
        <li><svg viewBox="0 0 24 24" aria-hidden="true"><path d="M2 5h20v14H2z M2 5l10 8 10-8" /></svg>info@LodgeBridgely.net</li>
        <li><svg viewBox="0 0 24 24" aria-hidden="true"><path d="M12 2a10 10 0 1 0 0 20 10 10 0 0 0 0-20zm0 2c.9 1.2 1.6 2.8 1.9 5h-3.8c.3-2.2 1-3.8 1.9-5zM4.3 9h3.8a17 17 0 0 0 0 6H4.3a8 8 0 0 1 0-6zm5.8 0h3.8a15 15 0 0 1 0 6h-3.8a15 15 0 0 1 0-6zm5.8 0h3.8a8 8 0 0 1 0 6h-3.8a17 17 0 0 0 0-6zM12 20c-.9-1.2-1.6-2.8-1.9-5h3.8c-.3 2.2-1 3.8-1.9 5z"/></svg>www.LodgeBridgely.net</li>
      </ul>
    </div>
    <div class="band-line upper"></div>
    <div class="tagline-band">Your company young and memorable message here</div>
    <div class="band-line lower"></div>
  </section>
</body>
</html>
```